Ridgeline Sawcutting, Inc. Business Card

Create a business card that is eye catching and based around concrete sawcutting. I've attached our current business card and logo for reference. We like aspects of the current business card, but it is starting to feel very loud and lost. We would like something that is still fun but is more modern and streamlined.

```html
<!DOCTYPE html>
<html lang="en">
<head>
<meta charset="utf-8">
<title>Ridgeline Sawcutting, Inc. Business Card</title>
<link href="https://fonts.googleapis.com/css2?family=Crimson+Pro:wght@600;700&display=swap" rel="stylesheet">
<style>
  :root {
    --page: #ece8e2;
    --card-dark: #151515;
    --card-mid: #2a2a2a;
    --navy: #1d2a6b;
    --brand-red: #8c1019;
    --ink: #111111;
    --white: #ffffff;
    --silver-hi: #f2f2f2;
    --silver-mid: #c4c4c4;
    --silver-lo: #8e8e8e;
  }
  * { margin: 0; padding: 0; box-sizing: border-box; }
  html, body { width: 1200px; height: 1200px; overflow: hidden; }
  body {
    background: var(--page);
    font-family: "Crimson Pro", Georgia, serif;
    position: relative;
  }
  .card {
    position: absolute;
    top: 315px;
    width: 462px;
    height: 773px;
    border-radius: 22px;
    background: radial-gradient(ellipse at 50% 45%, var(--card-mid), var(--card-dark) 75%);
    box-shadow: 0 6px 18px rgba(0,0,0,0.35);
    color: var(--white);
  }
  .card--front { left: 94px; }
  .card--back { left: 644px; }

  .pill {
    position: absolute;
    display: flex;
    align-items: center;
    justify-content: center;
    text-align: center;
    border-radius: 40px;
    background: linear-gradient(180deg, var(--silver-hi) 0%, var(--silver-mid) 45%, var(--silver-lo) 100%);
    box-shadow: 0 4px 8px rgba(0,0,0,0.5);
    font-weight: 700;
    text-transform: uppercase;
    line-height: 0.95;
  }
  .brand-mark {
    position: absolute;
    display: flex;
    align-items: center;
    justify-content: center;
    text-align: center;
    border-radius: 50%;
    background: var(--navy);
    color: var(--white);
    font-weight: 700;
    text-transform: uppercase;
    line-height: 1.05;
  }
  .brand-mark--front { left: 70px; top: 20px; width: 330px; height: 330px; font-size: 38px; padding: 40px; }
  .brand-mark--back { left: 95px; top: 136px; width: 274px; height: 274px; font-size: 32px; padding: 34px; }

  .name-pill { left: 21px; top: 373px; width: 422px; height: 81px; color: var(--brand-red); font-size: 40px; }
  .contact { position: absolute; left: 0; right: 0; text-align: center; font-weight: 700; }
  .contact--phones { top: 460px; font-size: 38px; line-height: 44px; }
  .contact--email { top: 562px; font-size: 25px; line-height: 34px; }
  .contact--address { top: 640px; font-size: 25px; line-height: 34px; }

  .phone-pill { left: 22px; top: 25px; width: 410px; height: 80px; color: var(--ink); font-size: 42px; }
  .service-pill { left: 56px; width: 343px; height: 66px; color: var(--brand-red); font-size: 34px; }
  .service-pill--small { font-size: 30px; }
</style>
</head>
<body>
  <section class="card card--front">
    <div class="brand-mark brand-mark--front">Ridgeline Sawcutting</div>
    <div class="pill name-pill">Dana Marlowe</div>
    <div class="contact contact--phones">
      <p>Office:&nbsp; 866.288.5463</p>
      <p>Cell:&nbsp; 201.555.0148</p>
    </div>
    <div class="contact contact--email">
      <p>Email:</p>
      <p>dana@ridgelineSawcutting.com</p>
    </div>
    <div class="contact contact--address">
      <p>Address:</p>
      <p>48 N. Harlow Ave</p>
      <p>Fairbrook, NJ 07699</p>
    </div>
  </section>

  <section class="card card--back">
    <div class="pill phone-pill">866 CUTLINE</div>
    <div class="brand-mark brand-mark--back">Ridgeline Sawcutting</div>
    <div class="pill service-pill" style="top:449px">Wall Sawing</div>
    <div class="pill service-pill" style="top:530px">Core Drilling</div>
    <div class="pill service-pill" style="top:612px">Slab Sawing</div>
    <div class="pill service-pill service-pill--small" style="top:690px">Breaking &amp;<br>Removal</div>
  </section>
</body>
</html>
```